Marlow Naturopathics business card design

Using the marlow logo designed, we would like that incorporated into a business card. A colour scheme which works with the logo and lists the following business details:

Dennis Marlow - Naturopath
Level 1, 58 Torvane Street
Wollongong NSW
(02) 4391 7084
www.dennismarlowhealth-example.com

We would also like space on the back of the card for next appointment times.

Target Market(s)

Anyone looking to improve their health

Industry/Entity Type

Business

Requirements
Must have
• Marlow Naturopathics logo, business details.
Nice to have
• Good colour schemes, attractive, eye-catching features that are easy to read.

```html
<!DOCTYPE html>
<html lang="en">
<head>
<meta charset="utf-8">
<title>Marlow Naturopathics – Business Card</title>
<link rel="stylesheet" href="https://fonts.googleapis.com/css2?family=Cinzel:wght@600&family=Arimo:wght@400&display=swap">
<style>
  :root {
    --card-white: #ffffff;
    --sky-light: #e3f3fd;
    --sky-mid: #9fd6f6;
    --sky-deep: #3aa3e6;
    --brand-blue: #1c5aa6;
    --wave-blue: #1f78cc;
    --wave-light: #7cc6f2;
    --accent-yellow: #f3f08a;
    --text-dark: #333333;
    --text-mid: #444444;
  }
  * { margin: 0; padding: 0; box-sizing: border-box; }
  html, body {
    width: 1200px;
    height: 666px;
    overflow: hidden;
    background: var(--card-white);
  }
  .card {
    position: relative;
    width: 1200px;
    height: 666px;
    overflow: hidden;
    background: var(--card-white);
  }
  .card-backdrop {
    position: absolute;
    inset: 0;
    width: 1200px;
    height: 666px;
  }
  .brand {
    position: absolute;
    left: 30px;
    top: 150px;
    width: 500px;
    text-align: center;
  }
  .brand-dot {
    display: block;
    width: 150px;
    height: 150px;
    margin: 0 auto 40px;
    border-radius: 50%;
    background: var(--brand-blue);
  }
  .brand-name {
    font-family: "Arimo", Arial, sans-serif;
    font-weight: 400;
    font-size: 42px;
    line-height: 1.2;
    color: var(--brand-blue);
  }
  .contact {
    position: absolute;
    right: 73px;
    top: 122px;
    text-align: right;
  }
  .contact-name {
    font-family: "Cinzel", Georgia, serif;
    font-weight: 600;
    font-size: 44px;
    letter-spacing: 1px;
    color: var(--brand-blue);
    line-height: 1;
  }
  .contact-role {
    font-family: "Arimo", Arial, sans-serif;
    font-size: 27px;
    color: var(--text-mid);
    margin-top: 14px;
  }
  .contact-address {
    font-family: "Arimo", Arial, sans-serif;
    font-style: normal;
    font-size: 29px;
    line-height: 46px;
    color: var(--text-dark);
    margin-top: 28px;
  }
  .contact-web {
    position: absolute;
    right: 73px;
    bottom: 22px;
    font-family: "Arimo", Arial, sans-serif;
    font-size: 29px;
    letter-spacing: 2.5px;
    color: var(--card-white);
  }
</style>
</head>
<body>
  <main class="card">
    <svg class="card-backdrop" viewBox="0 0 1200 666" aria-hidden="true">
      <defs>
        <radialGradient id="sky-glow" cx="0.3" cy="0.45" r="0.75">
          <stop offset="0" stop-color="#e3f3fd"/>
          <stop offset="0.55" stop-color="#9fd6f6"/>
          <stop offset="1" stop-color="#3aa3e6"/>
        </radialGradient>
        <linearGradient id="wave-deep" x1="0" y1="0" x2="1" y2="0">
          <stop offset="0" stop-color="#2a8ad8"/>
          <stop offset="1" stop-color="#1f78cc"/>
        </linearGradient>
      </defs>
      <path class="sky-panel" d="M0 0 H640 C520 120 470 300 560 470 C600 540 640 600 700 666 H0 Z" fill="url(#sky-glow)"/>
      <path class="sky-arc" d="M640 0 C520 120 470 300 560 470 C600 540 640 600 700 666" fill="none" stroke="#ffffff" stroke-width="14" opacity="0.85"/>
      <path class="sky-arc-soft" d="M600 0 C490 130 440 310 530 480 C570 560 610 610 650 666" fill="none" stroke="#ffffff" stroke-width="5" opacity="0.5"/>
      <path class="wave-light" d="M0 575 C320 540 720 470 1200 455 V666 H0 Z" fill="#7cc6f2"/>
      <path class="wave-accent" d="M0 590 C340 555 740 492 1200 480" fill="none" stroke="#f3f08a" stroke-width="7"/>
      <path class="wave-mid" d="M0 602 C350 570 760 505 1200 494 V666 H0 Z" fill="#ffffff" opacity="0.55"/>
      <path class="wave-deep" d="M0 615 C360 590 780 528 1200 518 V666 H0 Z" fill="url(#wave-deep)"/>
    </svg>

    <div class="brand">
      <span class="brand-dot"></span>
      <p class="brand-name">Marlow<br>Naturopathics</p>
    </div>

    <section class="contact">
      <h1 class="contact-name">Dennis Marlow</h1>
      <p class="contact-role">Naturopath</p>
      <address class="contact-address">
        Level 1, 58 Torvane Street<br>
        Wollongong NSW<br>
        (02) 4391 7084
      </address>
    </section>

    <p class="contact-web">www.dennismarlowhealth-example.com</p>
  </main>
</body>
</html>
```